Ironleaf Personal Training Studio Information Card

The front and back of card to give people that walk in to our gym. There are a few things to say on the card. But it also needs to be designed in an attractive way. You can make some of the information bullett points or with icons or graphics. Please look at our website at https://ironleaftraining.com/ . The card will be 4" x 9"

Target Market(s)

High End Clientele who want to train in a private gym

Industry/Entity Type

Fitness

Font styles to use
Serif
Sans Serif
Other font styles liked:
• the same font Velto uses on the zelpad

Colors
F0912C
F2A743
F7CA91
FBE8D2
FDF5EE

Requirements
Must have
• A cool look

```html
<!DOCTYPE html>
<html lang="en">
<head>
<meta charset="utf-8">
<title>Ironleaf Personal Training Studio – Information Card</title>
<link rel="stylesheet" href="https://fonts.googleapis.com/css2?family=Bebas+Neue&family=Rubik:ital,wght@0,400;0,500;0,700;1,400;1,500&display=swap">
<style>
  :root {
    --orange: #f04a14;
    --orange-warm: #f7871e;
    --ink: #4a4a4a;
    --ink-dark: #333333;
    --page: #e9e9ea;
    --card: #ffffff;
    --mist: #f1f1f1;
  }
  * { box-sizing: border-box; margin: 0; padding: 0; }
  html, body { width: 1200px; height: 1000px; overflow: hidden; }
  body { background: var(--page); font-family: "Rubik", Arial, sans-serif; color: var(--ink); position: relative; }

  .card { position: absolute; top: 75px; width: 378px; height: 850px; background: var(--card); overflow: hidden; box-shadow: 0 4px 16px rgba(0,0,0,.12); }
  .card--front { left: 210px; }
  .card--back { left: 611px; }
  .card-art { position: absolute; inset: 0; width: 378px; height: 850px; }
  .abs { position: absolute; }
  .display { font-family: "Bebas Neue", Impact, sans-serif; font-weight: 400; }
  .accent { color: var(--orange); }

  /* front */
  .brand { left: 0; width: 378px; top: 38px; text-align: center; }
  .brand-name { font-family: "Bebas Neue", Impact, sans-serif; font-size: 58px; line-height: 1; color: var(--ink); letter-spacing: 1px; }
  .brand-tag { font-family: "Rubik", Arial, sans-serif; font-weight: 500; font-size: 11px; letter-spacing: 5.4px; color: var(--ink); margin-top: 4px; }
  .promise { left: 0; width: 378px; top: 402px; text-align: center; font-size: 29px; line-height: 31px; color: var(--ink); }
  .member-photo { width: 102px; height: 102px; border-radius: 50%; border: 8px solid var(--orange); top: 468px; background: radial-gradient(circle at 50% 40%, #d9d6d3, #8c8480 70%, #5a5352); }
  .start-title { left: 0; width: 378px; top: 594px; text-align: center; font-size: 38px; color: var(--ink); line-height: 1; }
  .start-copy { left: 26px; width: 330px; top: 641px; font-size: 13.6px; line-height: 19.8px; color: var(--ink); }
  .start-copy strong { font-weight: 500; }

  /* back */
  .goals-kicker { left: 0; width: 378px; top: 112px; text-align: center; font-size: 21px; color: var(--ink-dark); letter-spacing: 1px; }
  .goals-kicker::before, .goals-kicker::after { content: ""; display: inline-block; width: 26px; height: 2px; background: var(--orange); vertical-align: middle; margin: 0 7px 4px; }
  .goals-title { left: 0; width: 378px; top: 130px; text-align: center; font-size: 46px; color: var(--orange); line-height: 1; }
  .goal { top: 196px; width: 63px; height: 68px; background: #fff; border-radius: 6px; box-shadow: 0 1px 4px rgba(0,0,0,.12); text-align: center; }
  .goal svg { display: block; margin: 9px auto 3px; width: 24px; height: 24px; }
  .goal-label { font-family: "Bebas Neue", Impact, sans-serif; font-size: 11.5px; line-height: 10.5px; color: var(--orange); }
  .tailor { left: 0; width: 378px; top: 289px; text-align: center; font-size: 29px; line-height: 28px; color: var(--ink-dark); }
  .tailor-sub { left: 0; width: 378px; top: 351px; text-align: center; font-size: 15px; letter-spacing: 2px; color: var(--orange); }
  .safety-copy { left: 28px; width: 322px; top: 398px; text-align: center; font-size: 11.2px; line-height: 17px; color: var(--ink-dark); }
  .safety-copy strong { font-weight: 500; }
  .rates-title { left: 27px; top: 532px; font-size: 37px; color: var(--orange); line-height: 1; }
  .rates-note { left: 28px; top: 578px; font-size: 11.5px; letter-spacing: 1px; color: var(--ink-dark); }
  .rate { top: 620px; color: var(--ink-dark); }
  .rate-price { font-weight: 700; font-size: 27px; line-height: 1; white-space: nowrap; }
  .rate-price .cur { font-size: 11px; font-weight: 400; }
  .rate-price .per { font-family: "Bebas Neue", Impact, sans-serif; font-weight: 400; font-size: 12px; }
  .rate-freq { font-size: 15px; line-height: 1; margin-top: 1px; white-space: nowrap; }
  .rate-divider { top: 620px; width: 1px; height: 50px; background: #777; }
  .partner-pill { left: 24px; top: 689px; width: 213px; height: 21px; border-radius: 11px; background: var(--orange); color: #fff; font-style: italic; font-size: 11.5px; line-height: 21px; padding-left: 14px; }
  .partner-example { left: 28px; top: 724px; width: 330px; font-size: 10.2px; line-height: 12.6px; color: var(--ink-dark); }
  .partner-example em { color: var(--orange); font-weight: 500; letter-spacing: .5px; }
  .handle { left: 0; width: 378px; top: 810px; text-align: center; font-family: "Rubik", Arial, sans-serif; font-weight: 700; font-size: 21px; letter-spacing: 4.6px; color: var(--ink-dark); }
  .handle-dot { left: 182px; top: 788px; width: 14px; height: 14px; border-radius: 50%; background: var(--orange); }
</style>
</head>
<body>

<section class="card card--front" aria-label="Card front">
  <svg class="card-art" viewBox="0 0 378 850" aria-hidden="true">
    <defs>
      <linearGradient id="flame" x1="0" x2="1" y1="0" y2="0">
        <stop offset="0" stop-color="#f04a14"/><stop offset=".5" stop-color="#f7871e"/><stop offset="1" stop-color="#f04a14"/>
      </linearGradient>
      <linearGradient id="mistFade" x1="0" x2="0" y1="0" y2="1">
        <stop offset="0" stop-color="#ebebeb"/><stop offset="1" stop-color="#f7f7f7"/>
      </linearGradient>
    </defs>
    <path d="M0,382 Q189,330 378,400 L378,590 L0,590 Z" fill="url(#mistFade)"/>
    <path d="M0,586 L378,586 L378,850 L0,850 Z" fill="#fff"/>
    <path d="M0,98 Q189,205 378,94 L378,125 Q189,245 0,130 Z" fill="url(#flame)"/>
    <path d="M0,330 Q189,315 378,352 L378,410 Q189,320 0,382 Z" fill="url(#flame)"/>
    <path d="M0,810 Q189,775 378,810 L378,850 L0,850 Z" fill="url(#flame)"/>
    <path d="M0,800 Q189,760 378,800 L378,808 Q189,770 0,808 Z" fill="#f57a1c"/>
  </svg>
  <div class="abs" role="img" aria-label="Photo of a trainer coaching a client through a cable exercise in the gym"
       style="left:0;top:0;width:378px;height:850px;clip-path:path('M0,140 Q189,225 378,142 L378,350 Q189,304 0,326 Z');background:linear-gradient(100deg,#7a6a6c 0%,#b5868a 35%,#4a3d3b 70%,#2b2526 100%);"></div>

  <div class="abs brand">
    <div class="brand-name">IRONLEAF</div>
    <div class="brand-tag">PRIVATE TRAINING STUDIO</div>
  </div>

  <h1 class="abs promise display"><span class="accent">A safe and individualized</span><br><span class="accent">approach</span> to strength training.</h1>

  <div class="abs member-photo" style="left:19px" role="img" aria-label="Photo of a client doing pull-ups with a trainer"></div>
  <div class="abs member-photo" style="left:138px" role="img" aria-label="Photo of an older client training with cables"></div>
  <div class="abs member-photo" style="left:257px" role="img" aria-label="Photo of two clients on treadmills"></div>

  <h2 class="abs start-title display">How do you <span class="accent">get started?</span></h2>
  <p class="abs start-copy"><strong>We schedule prospective clients for a no cost or obligation consultation.</strong> At that consultation we will do a movement screen with you. This will allow the trainer to see what level of flexibility and strength you are currently at. You will be able to discuss your goals and other issues (injuries, etc) at that time.</p>
</section>

<section class="card card--back" aria-label="Card back">
  <svg class="card-art" viewBox="0 0 378 850" aria-hidden="true">
    <defs>
      <linearGradient id="flameB" x1="0" x2="1" y1="0" y2="0">
        <stop offset="0" stop-color="#f04a14"/><stop offset=".5" stop-color="#f7871e"/><stop offset="1" stop-color="#f04a14"/>
      </linearGradient>
      <linearGradient id="gymFade" x1="0" x2="0" y1="0" y2="1">
        <stop offset="0" stop-color="#e2e2e2"/><stop offset="1" stop-color="#f6f6f6"/>
      </linearGradient>
    </defs>
    <path d="M0,258 Q189,200 378,258 L378,302 Q189,220 0,302 Z" fill="url(#flameB)"/>
    <rect x="0" y="764" width="378" height="10" fill="url(#flameB)"/>
  </svg>
  <div class="abs" role="img" aria-label="Photo of dumbbells and a kettlebell on a light wooden floor"
       style="left:0;top:0;width:378px;height:300px;clip-path:path('M0,0 L378,0 L378,258 Q189,200 0,258 Z');background:linear-gradient(180deg,#cfcfd0 0%,#e6e6e6 40%,#efefef 100%);"></div>
  <div class="abs" role="img" aria-label="Faded photo of the gym floor with training machines"
       style="left:0;top:519px;width:378px;height:245px;background:linear-gradient(180deg,#e4e4e4 0%,#eeeeee 60%,#f5f5f5 100%);"></div>

  <div class="abs goals-kicker display">Our clients have</div>
  <h2 class="abs goals-title display">Different goals:</h2>

  <div class="abs goal" style="left:20px">
    <svg viewBox="0 0 24 24"><path d="M12,2 a9,9 0 1 1 -0.1,0 Z" fill="#f04a14"/><circle cx="12" cy="9" r="4" fill="#fff"/><path d="M12,9 L13.5,6.5" stroke="#f04a14" stroke-width="1.4"/></svg>
    <div class="goal-label">Weight loss</div>
  </div>
  <div class="abs goal" style="left:88px">
    <svg viewBox="0 0 24 24" fill="#f04a14"><rect x="1" y="9" width="2" height="6"/><rect x="4" y="5" width="3" height="14"/><rect x="7" y="11" width="10" height="2"/><rect x="17" y="5" width="3" height="14"/><rect x="21" y="9" width="2" height="6"/></svg>
    <div class="goal-label">Build<br>strength</div>
  </div>
  <div class="abs goal" style="left:156px">
    <svg viewBox="0 0 24 24" fill="none" stroke="#f04a14" stroke-width="3" stroke-linecap="round"><circle cx="6" cy="4" r="2.4" fill="#f04a14" stroke="none"/><path d="M3,9 L11,6 L15,12 L20,21"/><path d="M13,10 L9,16"/></svg>
    <div class="goal-label">Increase<br>flexibility</div>
  </div>
  <div class="abs goal" style="left:223px">
    <svg viewBox="0 0 24 24" fill="none" stroke="#f04a14" stroke-width="3" stroke-linecap="round"><circle cx="13" cy="4" r="2.6" fill="#f04a14" stroke="none"/><path d="M4,20 L12,11 L17,16"/><path d="M3,22 L21,22"/></svg>
    <div class="goal-label">Functional<br>movements</div>
  </div>
  <div class="abs goal" style="left:291px">
    <svg viewBox="0 0 24 24" fill="none" stroke="#f04a14" stroke-width="2"><ellipse cx="9" cy="8" rx="6" ry="4"/><path d="M3,8 L3,18 L21,18 L21,12 L9,12"/><path d="M12,15 L12,18 M15,15 L15,18 M18,15 L18,18"/></svg>
    <div class="goal-label">Train for<br>an event</div>
  </div>

  <h2 class="abs tailor display">We will tailor<br>your training program</h2>
  <div class="abs tailor-sub display">To the specific results you are looking for</div>
  <p class="abs safety-copy">Some ways of training increase the chance of injury, <strong>we do not practice those types of training at <em>Ironleaf</em></strong>. Many of our clients have current or past injuries that can cause problems. We work with them to not aggravate those injuries or allow them to become an obstacle to their workouts.</p>

  <h2 class="abs rates-title display">Our rates:</h2>
  <div class="abs rates-note">All Sessions are 60 minutes</div>

  <div class="abs rate" style="left:28px">
    <div class="rate-price"><span class="cur">$</span>110<span class="per"> / SESSION</span></div>
    <div class="rate-freq display">1 time per week</div>
  </div>
  <div class="abs rate-divider" style="left:130px"></div>
  <div class="abs rate" style="left:155px">
    <div class="rate-price"><span class="cur">$</span>85<span class="per"> / SESSION</span></div>
    <div class="rate-freq display">2 time per week</div>
  </div>
  <div class="abs rate-divider" style="left:257px"></div>
  <div class="abs rate" style="left:277px">
    <div class="rate-price"><span class="cur">$</span>80<span class="per"> / SESSION</span></div>
    <div class="rate-freq display">3 time per week</div>
  </div>

  <div class="abs partner-pill">Add $40 for a Partnered Session</div>
  <p class="abs partner-example"><em>EXAMPLE:</em> A Partnered Session (2 people training together) coming twice a week is $125 per session</p>

  <div class="abs handle-dot" aria-hidden="true"></div>
  <div class="abs handle">IRONLEAFTRAINING</div>
</section>

</body>
</html>
```